1 Home page redesign for existing repair service site.

We need a refresh of our existing website that looks more 2017. We have made a mockup of the content that we want and a sample of where we want it. Nothing is set in stone, if you have better ideas of where things should go, feel free.

You can see our current site at http://www.mendora.example

The colors should stay orange/black/grey.

In many of the "boxes/banners" we will need images. Feel free to find in pixel vault as we have an account.

We have made notes throughout the wireframe that we have attached on what we are looking for. Let us know if you have any questions. Thanks.

Target Market(s)

People using technology and breaking it

Industry/Entity Type

It Service

Number of Pages Required

1 page

Font styles to use
Sans Serif

Requirements
Must have
• Must have a modern, professional look and feel. Need custom graphics and icons.

```html
<!DOCTYPE html>
<html lang="en">
<head>
<meta charset="utf-8">
<title>Mendora – Device Repair</title>
<link href="https://fonts.googleapis.com/css2?family=Open+Sans:wght@400;600;700;800&family=Oswald:wght@500;600&display=swap" rel="stylesheet">
<style>
:root{
  --orange:#f7931e;
  --orange-dark:#e07b0a;
  --black:#111;
  --dark:#1c1c1c;
  --dark2:#262626;
  --grey:#e9e9e9;
  --grey-mid:#8a8a8a;
  --white:#fff;
  --text:#333;
}
*{box-sizing:border-box;margin:0;padding:0}
html,body{width:1200px;height:2672px;overflow:hidden}
body{font-family:"Open Sans",Arial,sans-serif;color:var(--text);background:var(--white);font-size:13px}
.head{font-family:"Oswald","Arial Narrow",sans-serif;text-transform:uppercase;letter-spacing:.5px}
.wrap{width:1040px;margin:0 auto;position:relative;height:100%}
.btn{display:inline-block;background:var(--orange);color:var(--white);font-weight:700;font-size:11px;text-transform:uppercase;padding:7px 14px;border-radius:2px;white-space:nowrap}

.topbar{height:32px;background:var(--dark)}
.topbar .wrap{display:flex;justify-content:space-between;align-items:center}
.topbar .btn{padding:5px 12px;font-size:10px}

.header{height:88px;background:var(--white);border-bottom:1px solid #ddd}
.header .wrap{display:flex;align-items:center}
.brand{display:flex;align-items:center;gap:10px;font-weight:800;font-size:30px;color:var(--black)}
.brand .mark{width:30px;height:30px;background:var(--orange);border-radius:3px}
.header-actions{display:flex;gap:10px;margin-left:40px}
.phone-btn{background:var(--orange);color:#fff;font-weight:700;padding:8px 18px;font-size:12px}
.finder-btn{border:2px solid var(--orange);color:var(--orange);font-weight:700;padding:6px 14px;font-size:12px}
.nav{display:flex;gap:6px;margin-left:auto}
.nav a{background:var(--dark2);color:#fff;font-size:11px;font-weight:600;padding:8px 14px;text-decoration:none;text-transform:uppercase}

.hero{height:260px;background:linear-gradient(180deg,#2b2b2b 0%,#3a3632 45%,#1a1a1a 100%);position:relative;color:#fff;text-align:center}
.hero .caption{position:absolute;left:50%;top:80px;transform:translateX(-50%);background:rgba(0,0,0,.55);padding:16px 40px;white-space:nowrap}
.hero h1{font-size:30px;font-weight:600}
.hero p{font-size:15px;margin-top:4px}
.dots{position:absolute;left:50%;bottom:18px;transform:translateX(-50%);display:flex;gap:8px}
.dots span{width:9px;height:9px;border-radius:50%;background:#888}
.dots span:first-child{background:var(--orange)}

.counter{height:80px;background:var(--black);color:#fff}
.counter .wrap{display:flex;align-items:center;gap:26px}
.digits{display:flex;gap:5px}
.digits span{width:36px;height:48px;background:#fff;color:var(--black);font-size:32px;font-weight:700;display:flex;align-items:center;justify-content:center;border-radius:2px}
.counter p{font-size:18px;font-weight:700;text-transform:uppercase}

.promos{height:240px;padding-top:26px}
.promos .wrap{display:flex;gap:22px;height:196px}
.promo{flex:1;position:relative;background:var(--orange);display:flex;overflow:hidden}
.promo .txt{width:48%;padding:22px;color:#fff}
.promo h2{font-size:24px;line-height:1.1}
.promo p{font-size:12px;margin-top:10px;line-height:1.4}
.promo .photo{flex:1}
.promo.alt .txt{order:2;background:rgba(0,0,0,.15)}
.promo .btn{background:#fff;color:var(--orange);margin-top:14px}

.features{height:270px;background:var(--grey);padding-top:30px}
.features .wrap{display:flex;gap:20px;height:210px}
.feature{flex:1;background:linear-gradient(160deg,#3a3a3a,#161616);color:#fff;padding:20px;position:relative}
.feature h3{color:var(--orange);font-size:17px;line-height:1.15}
.feature p{font-size:12px;margin-top:12px;line-height:1.45;color:#ddd}
.feature .btn{position:absolute;left:20px;bottom:20px}

.title{text-align:center;color:var(--orange);font-size:22px;font-weight:600}
.title::after{content:"";display:block;width:60px;height:2px;background:var(--orange);margin:8px auto 0}

.repair{height:320px;padding-top:26px}
.tiles{display:grid;grid-template-columns:repeat(5,1fr);gap:18px 22px;margin-top:24px}
.tile{height:100px;background:var(--dark);display:flex;flex-direction:column}
.tile .ico{flex:1;display:flex;align-items:center;justify-content:center}
.tile .lbl{background:var(--orange);color:#fff;font-size:11px;font-weight:700;text-transform:uppercase;text-align:center;padding:5px 0;white-space:nowrap}

.cta{height:110px;background:linear-gradient(90deg,#222,#2f2f2f 50%,#1d1d1d)}
.cta .wrap{display:flex;align-items:center;justify-content:space-between;padding:0 60px}
.cta-item{display:flex;align-items:center;gap:14px;color:#fff;font-weight:700;font-size:14px;text-transform:uppercase}
.cta-item .circ{width:44px;height:44px;border-radius:50%;background:var(--orange);display:flex;align-items:center;justify-content:center}

.why{height:500px;padding-top:40px}
.cards{display:flex;gap:22px;margin-top:36px;position:relative}
.card{flex:1}
.card .photo{height:270px;background:linear-gradient(150deg,#cfcfcf,#8d8d8d)}
.card:nth-child(3) .photo{background:linear-gradient(150deg,#f2f2f2,#b8b8b8)}
.card:nth-child(4) .photo{background:linear-gradient(150deg,#6f8aa0,#2f3b45)}
.card:nth-child(5) .photo{background:linear-gradient(150deg,#dad5cd,#8a8377)}
.card .lbl{background:var(--orange);color:#fff;font-weight:700;font-size:13px;text-transform:uppercase;text-align:center;padding:0 10px;height:52px;display:flex;align-items:center;justify-content:center;line-height:1.3}
.arrow{position:absolute;top:125px;width:26px;height:26px;background:var(--dark);display:flex;align-items:center;justify-content:center}
.arrow.l{left:-36px}.arrow.r{right:-36px}

.testi{height:390px;background:linear-gradient(180deg,#2d2a26,#1a1916);padding-top:30px;position:relative}
.stars{text-align:center;color:var(--orange);font-size:14px;letter-spacing:3px;margin-top:8px}
.quotes{display:flex;gap:30px;margin-top:22px;padding:0 40px}
.quote{flex:1}
.quote .box{background:var(--orange);color:#fff;padding:16px 18px;font-size:12px;line-height:1.5;height:140px;overflow:hidden}
.quote .box b{display:block;text-align:center;margin-bottom:6px;font-size:12px}
.quote .who{color:#fff;font-size:12px;font-weight:700;margin-top:12px}
.testi .arrow{top:150px}
.share{display:block;width:380px;margin:28px auto 0;text-align:center;font-size:15px;padding:12px 0;background:var(--orange);color:#fff;font-weight:700}

.footer{height:350px;background:var(--dark);color:#bbb}
.contacts{display:flex;padding:28px 0 22px;border-bottom:1px solid #333}
.contact{flex:1;display:flex;gap:12px}
.contact .sq{width:32px;height:32px;background:var(--orange);flex:none;display:flex;align-items:center;justify-content:center}
.contact h4{color:#fff;font-size:13px}
.contact p{font-size:11px;margin-top:3px}
.cols{display:flex;padding-top:24px;gap:40px}
.col h5{color:var(--orange);font-size:13px;font-weight:700;margin-bottom:10px}
.col ul{list-style:none;font-size:11px;line-height:1.9}
.col.links{width:200px}
.col.blog{width:360px}
.col.blog p{font-size:11px;line-height:1.5;margin-bottom:10px}
.col.news{flex:1}
.subscribe{display:flex;margin:8px 0 14px}
.subscribe span{flex:1;background:#fff;color:#999;font-size:11px;padding:8px}
.subscribe b{background:var(--orange);color:#fff;font-size:11px;padding:8px 16px}
.social{display:flex;gap:10px;margin-top:8px}
.social i{width:20px;height:20px;border-radius:50%;background:#555;display:block}
.copy{height:32px;background:var(--black);color:#888;font-size:11px;text-align:center;line-height:32px}
</style>
</head>
<body>

<div class="topbar"><div class="wrap"><span class="btn">Get a quote</span><span class="btn">Track repair</span></div></div>

<header class="header"><div class="wrap">
  <div class="brand"><span class="mark"></span>Mendora</div>
  <div class="header-actions"><span class="phone-btn">210 555 0199</span><span class="finder-btn">Store Finder</span></div>
  <nav class="nav"><a>Repairs</a><a>Services</a><a>Get Quote</a><a>Blog</a></nav>
</div></header>

<section class="hero" role="img" aria-label="Photo of technicians repairing devices at a workshop">
  <div class="caption"><h1 class="head">20 Nationwide Locations</h1><p>There is one close to your town</p></div>
  <div class="dots"><span></span><span></span><span></span></div>
</section>

<section class="counter"><div class="wrap">
  <div class="digits"><span>0</span><span>1</span><span>2</span><span>3</span><span>4</span></div>
  <p>Repairs completed with happy customers. Yep, we fix a lot of devices!</p>
</div></section>

<section class="promos"><div class="wrap">
  <div class="promo">
    <div class="txt"><h2 class="head">20 Locations</h2><p>Find a store near you and walk in today for a free check.</p><span class="btn">Find a store</span></div>
    <div class="photo" role="img" aria-label="Photo of a hand holding a smartphone" style="background:linear-gradient(135deg,#9aa3ab,#4f585f)"></div>
  </div>
  <div class="promo alt">
    <div class="photo" role="img" aria-label="Photo of price charts on a screen" style="background:linear-gradient(135deg,#3b6ea0,#142c44)"></div>
    <div class="txt"><h2 class="head">Low Price Guarantee</h2><p>Find a lower price for the same repair and we will match it, no questions asked.</p><span class="btn">Learn more</span></div>
  </div>
</div></section>

<section class="features"><div class="wrap">
  <div class="feature"><h3 class="head">Open 7 days a week</h3><p>Our stores welcome you every day, including weekends and holidays.</p><span class="btn">Read more</span></div>
  <div class="feature"><h3 class="head">Free shipping on mail-in repairs</h3><p>Send your device to us and we cover the postage both ways.</p><span class="btn">Read more</span></div>
  <div class="feature"><h3 class="head">Accessories</h3><p>Cases, chargers and screen guards to keep your device safe.</p><span class="btn">Read more</span></div>
  <div class="feature"><h3 class="head">20 minute repairs</h3><p>Most screen and battery jobs are done while you wait.</p><span class="btn">Read more</span></div>
</div></section>

<section class="repair"><div class="wrap">
  <h2 class="title head">What we repair</h2>
  <div class="tiles">
    <div class="tile"><div class="ico"><svg width="28" height="46" viewBox="0 0 28 46"><rect x="2" y="2" width="24" height="42" rx="4" fill="none" stroke="#fff" stroke-width="2.5"/><circle cx="14" cy="38" r="2" fill="#fff"/></svg></div><div class="lbl">Smartphone Repair</div></div>
    <div class="tile"><div class="ico"><svg width="40" height="50" viewBox="0 0 40 50"><rect x="2" y="2" width="36" height="46" rx="4" fill="none" stroke="#fff" stroke-width="2.5"/><circle cx="20" cy="43" r="2" fill="#fff"/></svg></div><div class="lbl">Tablet Repair</div></div>
    <div class="tile"><div class="ico"><svg width="26" height="44" viewBox="0 0 26 44"><rect x="2" y="2" width="22" height="40" rx="4" fill="none" stroke="#fff" stroke-width="2.5"/></svg></div><div class="lbl">Music Player Repair</div></div>
    <div class="tile"><div class="ico"><svg width="28" height="46" viewBox="0 0 28 46"><rect x="2" y="2" width="24" height="42" rx="3" fill="#fff"/><rect x="5" y="6" width="18" height="30" fill="#1c1c1c"/></svg></div><div class="lbl">Android Phone Repair</div></div>
    <div class="tile"><div class="ico"><svg width="32" height="46" viewBox="0 0 32 46"><rect x="2" y="2" width="28" height="42" rx="3" fill="none" stroke="#fff" stroke-width="2.5"/><rect x="6" y="6" width="20" height="16" fill="#fff"/><g fill="#fff"><rect x="6" y="27" width="4" height="3"/><rect x="14" y="27" width="4" height="3"/><rect x="22" y="27" width="4" height="3"/><rect x="6" y="33" width="4" height="3"/><rect x="14" y="33" width="4" height="3"/><rect x="22" y="33" width="4" height="3"/></g></svg></div><div class="lbl">Keyboard Phone Repair</div></div>
    <div class="tile"><div class="ico"><svg width="52" height="46" viewBox="0 0 52 46"><rect x="2" y="2" width="48" height="32" rx="2" fill="none" stroke="#fff" stroke-width="2.5"/><path d="M20 34l-3 9h18l-3-9" fill="none" stroke="#fff" stroke-width="2.5"/></svg></div><div class="lbl">Desktop Repair</div></div>
    <div class="tile"><div class="ico"><svg width="60" height="40" viewBox="0 0 60 40"><rect x="9" y="2" width="42" height="28" rx="2" fill="none" stroke="#fff" stroke-width="2.5"/><path d="M2 34h56v3H2z" fill="#fff"/></svg></div><div class="lbl">Notebook Repair</div></div>
    <div class="tile"><div class="ico"><svg width="54" height="46" viewBox="0 0 54 46"><rect x="2" y="2" width="50" height="32" rx="2" fill="#fff"/><rect x="6" y="6" width="42" height="24" fill="#1c1c1c"/><rect x="18" y="38" width="18" height="4" fill="#fff"/></svg></div><div class="lbl">Computer Repair</div></div>
    <div class="tile"><div class="ico"><svg width="60" height="40" viewBox="0 0 60 40"><path d="M10 4h40v26H10z" fill="#fff"/><rect x="13" y="7" width="34" height="20" fill="#1c1c1c"/><path d="M2 32h56l-4 6H6z" fill="#fff"/></svg></div><div class="lbl">Laptop Repair</div></div>
    <div class="tile"><div class="ico"><svg width="58" height="36" viewBox="0 0 58 36"><path d="M14 4h30c8 0 12 6 12 16s-4 14-9 14c-5 0-7-7-11-7H22c-4 0-6 7-11 7-5 0-9-4-9-14S6 4 14 4z" fill="none" stroke="#fff" stroke-width="2.5"/><path d="M15 13v10M10 18h10" stroke="#fff" stroke-width="2.5"/><circle cx="41" cy="15" r="2" fill="#fff"/><circle cx="46" cy="20" r="2" fill="#fff"/></svg></div><div class="lbl">Console Repair</div></div>
  </div>
</div></section>

<section class="cta"><div class="wrap">
  <div class="cta-item"><span class="circ"><svg width="18" height="24" viewBox="0 0 18 24"><path d="M9 1a8 8 0 0 1 8 8c0 6-8 14-8 14S1 15 1 9a8 8 0 0 1 8-8z" fill="#fff"/><circle cx="9" cy="9" r="3" fill="#f7931e"/></svg></span>Find a store near you!</div>
  <div class="cta-item"><span class="circ"><svg width="24" height="18" viewBox="0 0 24 18"><rect x="1" y="1" width="22" height="16" fill="#fff"/><path d="M1 1l11 9 11-9" fill="none" stroke="#f7931e" stroke-width="2"/></svg></span>Mail in your device!</div>
  <div class="cta-item"><span class="circ"><svg width="22" height="22" viewBox="0 0 22 22"><path d="M3 8l8-6 8 6v12H3z" fill="#fff"/><rect x="9" y="13" width="4" height="7" fill="#f7931e"/></svg></span>Free pickup in store</div>
</div></section>

<section class="why"><div class="wrap">
  <h2 class="title head">Why choose Mendora</h2>
  <div class="cards">
    <span class="arrow l"><svg width="10" height="14"><path d="M8 1L2 7l6 6" fill="none" stroke="#fff" stroke-width="2"/></svg></span>
    <div class="card"><div class="photo" role="img" aria-label="Photo of a hand holding a phone in a store"></div><div class="lbl">Open 7 days a week</div></div>
    <div class="card"><div class="photo" role="img" aria-label="Photo of a phone package ready for shipping"></div><div class="lbl">Free shipping on mail-in repairs</div></div>
    <div class="card"><div class="photo" role="img" aria-label="Photo of phone accessories on a table"></div><div class="lbl">Accessories</div></div>
    <div class="card"><div class="photo" role="img" aria-label="Photo of tools opening a smartphone"></div><div class="lbl">20 minute repairs</div></div>
    <span class="arrow r"><svg width="10" height="14"><path d="M2 1l6 6-6 6" fill="none" stroke="#fff" stroke-width="2"/></svg></span>
  </div>
</div></section>

<section class="testi" role="img" aria-label="Background photo of hands typing on a laptop"><div class="wrap">
  <h2 class="title head">What our customers say</h2>
  <div class="stars">★★★★★</div>
  <span class="arrow l" style="left:0"><svg width="10" height="14"><path d="M8 1L2 7l6 6" fill="none" stroke="#fff" stroke-width="2"/></svg></span>
  <div class="quotes">
    <div class="quote"><div class="box"><b>Smartphone Repair</b>My screen was cracked badly and they fixed it in under half an hour. Friendly staff, fair price and the phone works like new. I will surely come back.</div><div class="who">Eleni K., Marousi</div></div>
    <div class="quote"><div class="box"><b>Tablet Repair</b>I mailed in my tablet on Monday and had it back by Thursday. Shipping was free and they kept me updated at every step of the repair.</div><div class="who">Eleni K., Marousi</div></div>
    <div class="quote"><div class="box"><b>Laptop Repair</b>The battery on my laptop died suddenly. The team replaced it the same day and even cleaned the fan. Great service from start to finish.</div><div class="who">Eleni K., Marousi</div></div>
  </div>
  <span class="arrow r" style="right:0"><svg width="10" height="14"><path d="M2 1l6 6-6 6" fill="none" stroke="#fff" stroke-width="2"/></svg></span>
  <span class="share">Tell us about your Mendora experience</span>
</div></section>

<footer class="footer"><div class="wrap">
  <div class="contacts">
    <div class="contact"><span class="sq"><svg width="16" height="12"><rect x="1" y="1" width="14" height="10" fill="none" stroke="#fff" stroke-width="1.5"/><path d="M1 1l7 6 7-6" fill="none" stroke="#fff" stroke-width="1.5"/></svg></span><div><h4>Email Support</h4><p>We usually respond within 24 hours.</p><p>help@mendora.example</p></div></div>
    <div class="contact"><span class="sq"><svg width="14" height="14"><path d="M3 1l3 3-2 2c1 2 2 3 4 4l2-2 3 3-2 2C6 13 1 8 1 3z" fill="#fff"/></svg></span><div><h4>Contact our call center</h4><p>Call to speak to an expert today.</p><p>210 555 0199</p></div></div>
    <div class="contact"><span class="sq"><svg width="16" height="14"><path d="M1 1h14v9H6l-4 3v-3H1z" fill="#fff"/></svg></span><div><h4>Live Chat</h4><p>Chat with an expert technician now.</p><p>Mon to Sun, 9:00 to 21:00</p></div></div>
  </div>
  <div class="cols">
    <div class="col links"><h5>Quick links</h5><ul><li>About Mendora</li><li>Business Services</li><li>Locations &amp; Hours</li><li>Low Price Guarantee</li><li>Shipping Instructions</li><li>Warranty Policy</li><li>Frequently Asked Questions</li></ul></div>
    <div class="col blog"><h5>Mendora blog</h5><p>Five simple habits that keep your phone battery healthy for longer. Read our tips on charging, heat and storage before your next trip.</p><p>What to do when your device gets wet: quick steps that can save your phone from water damage before you bring it to our store.</p></div>
    <div class="col news"><h5>Sign up for newsletter</h5><p style="font-size:11px">Subscribe to our latest newsletter</p><div class="subscribe"><span>Email Address</span><b>Send</b></div><h5>We're Social</h5><div class="social"><i></i><i></i><i></i><i></i><i></i><i></i></div></div>
  </div>
</div></footer>
<div class="copy">© Mendora 2017</div>

</body>
</html>
```